Residential Roofing Company

Website for Residential roofing company. Servicing Minnesota (Hennepin, Anoka, Sherburne County). Located in Ramsey, Minnesota. Asphalt Shingles (TLR and Palder Brisk Manufacturers)

Target Market(s)

Storm Damage repair. Roof Replacement and Repair.

Industry/Entity Type

Residential Roofing

Coding

Coded - Design and coding required

Number of Pages Required

5+ page

Colors

Designer to choose colors to be used in the design.

Requirements
Should not have
• No Commercial Roofing

```html
<!DOCTYPE html>
<html lang="en">
<head>
<meta charset="utf-8">
<title>Kestrel Roofing</title>
<link href="https://fonts.googleapis.com/css2?family=Audiowide&family=Roboto:wght@400;500;700&display=swap" rel="stylesheet">
<style>
:root{
  --blue:#0b49a8;
  --blue-dark:#083a8c;
  --cyan:#1a9ad8;
  --ink:#222;
  --grey-text:#8a8a8a;
  --dark:#2f2f2f;
  --light:#f4f4f4;
  --white:#fff;
}
*{box-sizing:border-box;margin:0;padding:0}
html,body{width:1200px;height:3897px;overflow:hidden}
body{position:relative;font-family:"Roboto",sans-serif;color:var(--ink);background:var(--white)}
.abs{position:absolute}
.btn{position:absolute;display:flex;align-items:center;justify-content:center;color:var(--white);font-weight:700;font-size:14px;text-transform:uppercase;background:linear-gradient(90deg,var(--blue),var(--cyan))}
.section-title{position:absolute;left:0;width:1200px;text-align:center;font-family:"Audiowide",sans-serif;font-size:40px;letter-spacing:1px}
.topbar{top:0;left:0;width:1200px;height:48px;background:linear-gradient(90deg,var(--blue-dark),var(--cyan))}
.topbar-left{top:0;left:0;width:462px;height:48px;background:var(--dark);clip-path:polygon(0 0,100% 0,calc(100% - 40px) 100%,0 100%)}
.topbar-text{top:15px;font-size:14px;color:var(--white)}
.social{position:absolute;width:32px;height:32px;border-radius:50%;background:var(--white)}
.logo{font-size:30px;font-weight:700;color:var(--blue);letter-spacing:1px}
.nav{top:87px;left:458px;display:flex;gap:34px;font-size:16px;font-weight:500}
.nav .active{color:var(--cyan)}
.hero-photo{top:145px;left:0;width:1200px;height:642px;background:linear-gradient(180deg,#7aa6d6 0%,#b9cfe4 30%,#7d8794 55%,#5a6b4a 85%,#3f6a2e 100%);clip-path:polygon(0 0,100% 0,100% 516px,50% 642px,0 516px)}
.hero-title{top:368px;left:0;width:1200px;text-align:center;font-family:"Audiowide",sans-serif;font-size:38px;font-weight:400;color:var(--white)}
.hero-sub{top:425px;left:320px;width:560px;text-align:center;font-size:16px;line-height:27px;color:var(--white);font-weight:500}
.arrow-tab{position:absolute;top:392px;width:24px;height:36px;background:var(--white)}
.about-frame{top:1059px;left:110px;width:356px;height:318px;border:6px solid var(--blue);border-top:none;border-right:none}
.about-frame-right{top:1327px;left:460px;width:6px;height:50px;background:var(--cyan)}
.about-p{left:647px;width:441px;font-size:13.5px;line-height:25.5px;color:var(--grey-text);text-align:justify}
.services-band{top:1492px;left:0;width:1200px;height:402px;background:linear-gradient(100deg,#1c4fb0 0%,#2a72c8 55%,#2aa1dc 100%)}
.card{position:absolute;top:1681px;width:309px;height:425px;background:var(--white);box-shadow:0 2px 10px rgba(0,0,0,.12);padding:6px}
.card-photo{width:297px;height:203px}
.card-icon{position:absolute;left:119px;top:172px;width:72px;height:72px;border-radius:50%;background:linear-gradient(135deg,var(--blue),var(--cyan));border:4px solid var(--white)}
.card h3{margin-top:52px;text-align:center;font-size:17px;font-weight:500;text-transform:uppercase}
.card p{margin:12px 14px 0;text-align:center;font-size:12.5px;line-height:23px;color:var(--grey-text)}
.card .more{margin-top:12px;text-align:center;font-size:13px;font-weight:700;color:var(--blue)}
.contact-bg{top:2994px;left:0;width:1200px;height:620px;background:var(--light)}
.field{position:absolute;background:var(--white);box-shadow:0 1px 6px rgba(0,0,0,.1);font-size:15px;color:#666;padding:16px 18px}
.footer-nav{top:3662px;left:0;width:1200px;display:flex;justify-content:center;gap:28px;font-size:16px;font-weight:500;color:var(--white)}
.footer-rule{top:3705px;left:110px;width:978px;height:1px;background:#4a4a4a}
.f-circle{position:absolute;top:3722px;width:76px;height:76px;border-radius:50%;background:var(--white);display:flex;align-items:center;justify-content:center}
.f-label{position:absolute;top:3744px;font-size:14px;font-weight:700;color:var(--white)}
.f-value{position:absolute;top:3772px;font-size:14px;color:#bbb}
.f-div{position:absolute;top:3722px;width:1px;height:90px;background:#4a4a4a}
</style>
</head>
<body>

<div class="abs topbar"></div>
<div class="abs topbar-left"></div>
<div class="abs topbar-text" style="left:110px">Email Us:&nbsp; office@kestrelroofing.com</div>
<div class="abs topbar-text" style="left:800px">Call Us:&nbsp; 612-555-0147</div>
<div class="social" style="left:977px;top:8px"></div>
<div class="social" style="left:1016px;top:8px"></div>
<div class="social" style="left:1055px;top:8px"></div>

<div class="abs logo" style="left:110px;top:76px">KESTREL ROOFING</div>
<nav class="abs nav">
  <span class="active">HOME</span><span>ABOUT</span><span>SERVICES</span><span>PROJECTS</span><span>CONTACT</span>
</nav>
<div class="btn" style="left:968px;top:72px;width:120px;height:49px;background:linear-gradient(90deg,var(--blue-dark),var(--cyan))">Careers</div>

<svg class="abs" style="top:640px;left:0" width="1200" height="180" viewBox="0 0 1200 180">
  <defs><linearGradient id="hg" x1="0" x2="1"><stop offset="0" stop-color="#0b49a8"/><stop offset="1" stop-color="#1a9ad8"/></linearGradient></defs>
  <polygon points="0,21 600,147 1200,21 1200,27 600,160 0,27" fill="url(#hg)"/>
  <polygon points="0,40 600,164 1200,40 1200,46 600,177 0,46" fill="url(#hg)"/>
</svg>
<div class="abs hero-photo" role="img" aria-label="Photo of a grey two-storey suburban house with a new shingle roof under a blue sky"></div>
<div class="arrow-tab" style="left:0;clip-path:polygon(0 0,100% 50%,0 100%)"></div>
<div class="arrow-tab" style="left:1176px;clip-path:polygon(100% 0,0 50%,100% 100%)"></div>
<h1 class="abs hero-title">LEADERS IN QUALITY ROOFING</h1>
<p class="abs hero-sub">With over 40 years of experience in servicing the residents of the Twin<br>Cities area, the Kestrel Roofing team knows</p>
<div class="btn" style="left:531px;top:505px;width:136px;height:46px">Get Started</div>

<div class="abs about-frame"></div>
<div class="abs about-frame-right"></div>
<div class="abs" style="left:188px;top:899px;width:296px;height:334px;background:linear-gradient(180deg,#6fa4de,#5d6671 45%,#9a7a5e 75%,#4f7a3a)" role="img" aria-label="Photo of a stone and siding family home"></div>
<div class="abs" style="left:344px;top:1062px;width:234px;height:260px;background:var(--white)"></div>
<div class="abs" style="left:350px;top:1068px;width:222px;height:248px;background:linear-gradient(180deg,#b9cde0,#6b7480 40%,#55606a 75%,#4d7a35)" role="img" aria-label="Photo of a grey sided house with dormer windows"></div>
<h2 class="abs" style="left:647px;top:952px;font-family:'Audiowide',sans-serif;font-size:40px;font-weight:400">ABOUT US</h2>
<p class="abs about-p" style="top:1027px">With over 40 years of experience in servicing the residents of the Twin Cities area, the Kestrel Roofing team knows what it takes to get the job done right! We are a second generation roofing company that has instilled a modern touch into our brand. Kestrel Roofing is a Woman Owned and Operated Company.</p>
<p class="abs about-p" style="top:1163px">We've implemented the knowledge &amp; successful business practices from our history and experience into our brand. Roofing is our history and we strive to make sure our customers receive the best experience possible.</p>
<div class="btn" style="left:647px;top:1295px;width:133px;height:46px">Learn More</div>

<div class="abs services-band"></div>
<h2 class="section-title" style="top:1585px;color:var(--white);font-weight:400">OUR SERVICES</h2>

<div class="card" style="left:110px">
  <div class="card-photo" style="background:linear-gradient(135deg,#6c6f74,#9aa0a6 50%,#c8b48a)" role="img" aria-label="Photo of a roofer nailing shingles"></div>
  <div class="card-icon"></div>
  <h3>Storm Damage Repair</h3>
  <p>Sed ut perspiciatis unde omnis iste natus error sit voluptatem accusantium doloremque laudantium totam aperiam.</p>
  <div class="more">READ MORE &nbsp;»</div>
</div>
<div class="card" style="left:445px">
  <div class="card-photo" style="background:linear-gradient(180deg,#8fb6e0,#5f7a4a 45%,#6d7580 70%,#5a6470)" role="img" aria-label="Photo of a house roof with dormers among trees"></div>
  <div class="card-icon"></div>
  <h3>Roof Replacement &amp; Repair</h3>
  <p>Kestrel specializes in Residential roofing. With over 40 years of experience and 2 generations in the industry, we can assist you</p>
  <div class="more">READ MORE &nbsp;»</div>
</div>
<div class="card" style="left:779px">
  <div class="card-photo" style="background:linear-gradient(135deg,#4a5058,#7c8590 50%,#b8b2a6 80%,#6a7a4a)" role="img" aria-label="Photo of a modern house entrance with siding and windows"></div>
  <div class="card-icon"></div>
  <h3>Siding / Windows</h3>
  <p>Sed ut perspiciatis unde omnis iste natus error sit voluptatem accusantium doloremque laudantium totam aperiam.</p>
  <div class="more">READ MORE &nbsp;»</div>
</div>

<h2 class="section-title" style="top:2258px;font-weight:400">OUR PROJECTS</h2>
<div class="abs" style="left:110px;top:2354px;width:480px;height:283px;background:linear-gradient(180deg,#5c88c4,#6a5a4a 45%,#c8c0ae 75%,#7a8a60)" role="img" aria-label="Photo of a row of townhouse gables"></div>
<div class="abs" style="left:608px;top:2354px;width:480px;height:283px;background:radial-gradient(circle at 50% 45%,#8a8490 0 30%,#6a8a4a 55%,#3d5a2a)" role="img" aria-label="Aerial photo of a new grey roof"></div>
<div class="abs" style="left:110px;top:2652px;width:317px;height:232px;background:linear-gradient(135deg,#8a6654,#a88472 50%,#7a5a4c)" role="img" aria-label="Close-up photo of roof shingles"></div>
<div class="abs" style="left:442px;top:2652px;width:315px;height:232px;background:linear-gradient(135deg,#4c6a3a,#7a8070 50%,#4a6a38)" role="img" aria-label="Aerial photo of a residential neighbourhood"></div>
<div class="abs" style="left:773px;top:2652px;width:315px;height:232px;background:linear-gradient(135deg,#2e4a26,#9a968c 45%,#b8b2a6)" role="img" aria-label="Photo of a shingled roof slope with vents"></div>

<div class="abs contact-bg"></div>
<h2 class="section-title" style="top:3072px;font-weight:400">CONTACT US</h2>
<div class="field" style="left:139px;top:3176px;width:300px;height:48px">Full Name</div>
<div class="field" style="left:449px;top:3176px;width:300px;height:48px">Phone</div>
<div class="field" style="left:760px;top:3176px;width:299px;height:48px">Email Address</div>
<div class="field" style="left:139px;top:3238px;width:920px;height:92px">Message</div>
<div class="btn" style="left:520px;top:3347px;width:159px;height:45px;background:var(--blue)">Send Message</div>

<svg class="abs" style="top:3440px;left:0" width="1200" height="457" viewBox="0 0 1200 457">
  <defs><linearGradient id="fg" x1="0" x2="1"><stop offset="0" stop-color="#0b49a8"/><stop offset="1" stop-color="#1a9ad8"/></linearGradient></defs>
  <polygon points="0,170 600,13 1200,170 1200,457 0,457" fill="url(#fg)"/>
  <polygon points="0,178 600,27 1200,178 1200,457 0,457" fill="#f4f4f4"/>
  <polygon points="0,184 600,33 1200,184 1200,457 0,457" fill="url(#fg)"/>
  <polygon points="0,194 600,43 1200,194 1200,457 0,457" fill="#2f2f2f"/>
</svg>
<div class="abs logo" style="left:0;top:3578px;width:1200px;text-align:center;color:var(--white)">KESTREL ROOFING</div>
<nav class="abs footer-nav">
  <span>HOME</span><span>/</span><span>ABOUT</span><span>/</span><span>SERVICES</span><span>/</span><span>PROJECTS</span><span>/</span><span>CONTACT</span>
</nav>
<div class="abs footer-rule"></div>

<div class="f-circle" style="left:110px">
  <svg width="34" height="34" viewBox="0 0 24 24"><path d="M12 2a7 7 0 0 0-7 7c0 5 7 13 7 13s7-8 7-13a7 7 0 0 0-7-7zm0 9.5A2.5 2.5 0 1 1 12 6.5a2.5 2.5 0 0 1 0 5z" fill="#0b49a8"/></svg>
</div>
<div class="f-label" style="left:210px">LOCATION:</div>
<div class="f-value" style="left:210px">Cedar Hollow, ND 58000</div>
<div class="f-div" style="left:425px"></div>

<div class="f-circle" style="left:504px">
  <svg width="32" height="32" viewBox="0 0 24 24"><path d="M6.6 10.8a15 15 0 0 0 6.6 6.6l2.2-2.2a1 1 0 0 1 1-.25 11.4 11.4 0 0 0 3.6.6 1 1 0 0 1 1 1V20a1 1 0 0 1-1 1A17 17 0 0 1 3 4a1 1 0 0 1 1-1h3.5a1 1 0 0 1 1 1c0 1.25.2 2.45.6 3.6a1 1 0 0 1-.25 1z" fill="#0b49a8"/></svg>
</div>
<div class="f-label" style="left:604px">PHONE:</div>
<div class="f-value" style="left:604px">612-555-0147</div>
<div class="f-div" style="left:775px"></div>

<div class="f-circle" style="left:836px">
  <svg width="34" height="34" viewBox="0 0 24 24"><rect x="2" y="5" width="20" height="14" rx="2" fill="#0b49a8"/><path d="M3 6l9 7 9-7" stroke="#fff" stroke-width="1.6" fill="none"/></svg>
</div>
<div class="f-label" style="left:936px">EMAIL:</div>
<div class="f-value" style="left:936px">office@kestrelroofing.com</div>

<div class="abs" style="top:3858px;left:0;width:1200px;text-align:center;font-size:12px;color:var(--white)">© 2022 <b>KESTREL ROOFING</b> &nbsp;|&nbsp; All Rights Reserved</div>
<div class="social" style="left:979px;top:3852px;background:var(--blue)"></div>
<div class="social" style="left:1016px;top:3852px"></div>
<div class="social" style="left:1054px;top:3852px"></div>

</body>
</html>
```